Jolly Paws Business Card Update

I have a business card which I love. I want to keep the same logo, colours, font and style. I want to upgrade the scripting and remove some elements and add others.
On the front side under Services - remove the existing wording and insert - Providing individual coaching strategies to create happy, healthy and social canine companions
Under Rebecca Thornbury amend the current wording to read: Qualified in Dog Behavioural Training, Natural Animal Healthcare and Animal Health Science
On the reverse side to remove the web address.

```html
<!DOCTYPE html>
<html lang="en">
<head>
<meta charset="utf-8">
<title>Jolly Paws Business Card</title>
<link rel="stylesheet" href="https://fonts.googleapis.com/css2?family=Archivo:wght@400;500;700;800&display=swap">
<style>
  :root {
    --backdrop: #d8d8d8;
    --sky: #00a6e4;
    --royal: #0a5cbf;
    --navy: #23298a;
    --cream: #f3ecd2;
    --red-bright: #e8100f;
    --red-deep: #6e0f0c;
    --white: #ffffff;
  }
  * { margin: 0; padding: 0; box-sizing: border-box; }
  html, body {
    width: 1200px; height: 846px; overflow: hidden;
    background: var(--backdrop);
    font-family: "Archivo", Arial, sans-serif;
  }
  .canvas {
    position: relative; width: 1200px; height: 846px;
    display: flex; align-items: center; justify-content: center; gap: 30px;
  }
  .card {
    width: 555px; height: 317px; display: block;
    box-shadow: 0 10px 24px rgba(0,0,0,0.22);
  }
  .card text { font-family: "Archivo", Arial, sans-serif; fill: var(--white); }
  .services-title { font-weight: 800; font-size: 14px; }
  .services-copy { font-weight: 400; font-size: 12px; }
  .strap { font-weight: 500; font-size: 10px; fill: #3a1a12 !important; }
  .holder-name { font-weight: 800; font-size: 14px; }
  .contact { font-weight: 500; font-size: 11.5px; }
  .credentials { font-weight: 400; font-size: 8.6px; }
  .brand-small { font-weight: 700; font-size: 15px; }
  .brand-large { font-weight: 800; font-size: 34px; letter-spacing: 1px; }
  .tagline { font-weight: 500; font-size: 13px; letter-spacing: 0.6px; }
</style>
</head>
<body>
<main class="canvas">

  <!-- Front: services and contact -->
  <svg class="card card-front" viewBox="0 0 555 317" aria-label="Jolly Paws business card, front">
    <defs>
      <linearGradient id="blueField" x1="0" y1="0" x2="1" y2="1">
        <stop offset="0" stop-color="var(--sky)"/>
        <stop offset="0.45" stop-color="var(--sky)"/>
        <stop offset="0.75" stop-color="var(--royal)"/>
        <stop offset="1" stop-color="var(--navy)"/>
      </linearGradient>
      <linearGradient id="redBand" x1="0" y1="0" x2="1" y2="0">
        <stop offset="0" stop-color="var(--red-deep)"/>
        <stop offset="0.45" stop-color="var(--red-bright)"/>
        <stop offset="1" stop-color="var(--red-deep)"/>
      </linearGradient>
      <path id="strapLine" d="M0,241 Q280,186 555,161"/>
    </defs>
    <rect class="field" width="555" height="317" fill="url(#blueField)"/>
    <path class="cream-strip" d="M0,230 Q280,175 555,150 L555,170 Q280,195 0,250 Z" fill="var(--cream)"/>
    <path class="red-band" d="M0,248 Q280,193 555,168 L555,317 L0,317 Z" fill="url(#redBand)"/>

    <g class="brand-mark">
      <circle cx="92" cy="110" r="32" fill="var(--cream)"/>
      <text class="brand-small" x="92" y="166" text-anchor="middle">Jolly Paws</text>
    </g>
    <line class="divider" x1="172" y1="62" x2="172" y2="160" stroke="var(--white)" stroke-width="1.2"/>

    <g class="services">
      <text class="services-title" x="188" y="74">SERVICES</text>
      <text class="services-copy" x="196" y="93">Providing individual</text>
      <text class="services-copy" x="196" y="108">coaching strategies to</text>
      <text class="services-copy" x="196" y="123">create happy, healthy and</text>
      <text class="services-copy" x="196" y="138">social canine companions</text>
    </g>

    <text class="strap"><textPath href="#strapLine" startOffset="60">promoting communication and connection between dogs and their families</textPath></text>

    <g class="contact-block" transform="rotate(-6 300 250)">
      <text class="holder-name" x="300" y="232" text-anchor="middle">Rebecca Thornbury</text>
      <g class="phone">
        <circle cx="178" cy="252" r="6" fill="var(--white)"/>
        <rect x="175.5" y="248" width="5" height="8" rx="1" fill="var(--red-bright)"/>
        <text class="contact" x="188" y="256">0400 128 653</text>
      </g>
      <g class="email">
        <circle cx="276" cy="252" r="6" fill="var(--white)"/>
        <rect x="272.5" y="249.5" width="7" height="5" fill="none" stroke="var(--red-bright)" stroke-width="1"/>
        <path d="M272.5,249.5 L276,252.5 L279.5,249.5" fill="none" stroke="var(--red-bright)" stroke-width="1"/>
        <text class="contact" x="286" y="256">hello@jollypawsdogs.com</text>
      </g>
      <text class="credentials" x="306" y="276" text-anchor="middle">Qualified in Dog Behavioural Training, Natural Animal Healthcare and Animal Health Science</text>
    </g>
  </svg>

  <!-- Back: brand -->
  <svg class="card card-back" viewBox="0 0 555 317" aria-label="Jolly Paws business card, back">
    <defs>
      <linearGradient id="blueFieldBack" x1="0" y1="0" x2="1" y2="1">
        <stop offset="0" stop-color="var(--sky)"/>
        <stop offset="0.45" stop-color="var(--sky)"/>
        <stop offset="0.72" stop-color="var(--royal)"/>
        <stop offset="1" stop-color="var(--navy)"/>
      </linearGradient>
      <linearGradient id="redSwoosh" x1="0" y1="1" x2="1" y2="0">
        <stop offset="0" stop-color="var(--red-deep)"/>
        <stop offset="0.45" stop-color="var(--red-bright)"/>
        <stop offset="1" stop-color="var(--red-deep)"/>
      </linearGradient>
    </defs>
    <rect class="field" width="555" height="317" fill="url(#blueFieldBack)"/>
    <path class="cream-strip" d="M62,317 Q300,196 555,136 L555,146 Q305,206 74,317 Z" fill="var(--cream)"/>
    <path class="red-swoosh" d="M74,317 Q305,206 555,146 L555,317 Z" fill="url(#redSwoosh)"/>

    <g class="brand-mark">
      <circle cx="180" cy="120" r="46" fill="var(--cream)"/>
      <text class="brand-large" x="240" y="140">Jolly Paws</text>
      <text class="tagline" x="244" y="162">HAPPY DOGS, HAPPY OWNERS</text>
    </g>
  </svg>

</main>
</body>
</html>
```